This project is to address Personal Life issues/ Health & Wellness using a certified Professional Coaching Approach.

Major coaching areas include: Weight loss, Overwhelm/ Time Management, Increased Energy, Leadership, Improved Relationships, Finding Your Life Purpose & passion, Self Esteem & Confidence,

The combination of a board certified Internal Medicine physician and
professional coach is a powerful and unique approach to help people achieve
better health and well being.

Target Market(s)

Existing or potentially new patients/clients interested in any of the listed categories of coaching.

Industry/Entity Type

Life Coaching

Font styles to use
Sans Serif

Colors
00a990
0292cd
0255a3
33b8a4
a64599
6b449b
876aae
3176b5
33a6d7

Requirements
Must have
• Design specifics: Use of deep blues/greens using nature imagery is
• preferred- see our website for at Brightvalecaredoc.com
• Each category of coaching must be listed out with a paragraph of description below each- I will provide the description in an attachment that is pending.
• Title of Brochure: "Clearbrook Health Personal Life & Wellness Coaching."
• "Coaching That Works!"
Nice to have
• A definition of coaching on the front of brochure:
• " A compassionate catalyzing relationship - The art of facilitating the performance, learning and development of another so they may achieve what the want faster.”
• Also on the front please place: "Stuck? Ask about a free coaching consult with Dr. Tavren to learn more!"
Should not have
• Should not have anything in the brochure that mentions medical services from the website outside of weight loss. The purpose of the brochure is to promote the coaching services.

```html
<!DOCTYPE html>
<html lang="en">
<head>
<meta charset="utf-8">
<title>Clearbrook Health Coaching Brochure</title>
<link rel="stylesheet" href="https://fonts.googleapis.com/css2?family=Cutive&family=Oswald:wght@300;400&display=swap">
<style>
  :root {
    --page-bg: #e2e2e2;
    --panel-bg: #ffffff;
    --ink: #111111;
    --ink-soft: #2a2a2a;
    --forest-green: #3b5a18;
    --deep-navy: #0b2646;
    --navy-note-text: #c9d8e8;
    --bullet: #0d2a48;
    --forest-dark: #3f4f2e;
    --forest-mid: #7d8c66;
    --forest-light: #c3c9b3;
  }
  * { margin: 0; padding: 0; box-sizing: border-box; }
  html, body { width: 1200px; height: 899px; overflow: hidden; }
  body { background: var(--page-bg); position: relative; font-family: 'Oswald', sans-serif; color: var(--ink); }

  .panel { position: absolute; top: 5px; height: 881px; }

  /* Left: coaching areas */
  .panel-areas { left: 8px; width: 373px; overflow: hidden; }
  .forest-backdrop {
    position: absolute; inset: 0;
    background:
      radial-gradient(ellipse at 50% 50%, rgba(230,232,210,0.6), transparent 55%),
      linear-gradient(165deg, var(--forest-dark) 0%, var(--forest-mid) 35%, var(--forest-light) 60%, var(--forest-mid) 85%, var(--forest-dark) 100%);
  }
  .forest-veil { position: absolute; inset: 0; background: rgba(255,255,255,0.5); }
  .areas-content { position: relative; padding: 27px 0 0 22px; }
  .areas-title { font-family: 'Cutive', serif; font-size: 29px; line-height: 36px; font-weight: 400; }
  .areas-list { list-style: none; margin-top: 40px; }
  .areas-list li { font-size: 28px; line-height: 29px; margin-bottom: 19px; letter-spacing: -0.3px; }

  /* Middle: coaching services */
  .panel-coaching { left: 408px; width: 371px; background: var(--panel-bg); }
  .coaching-title { font-family: 'Cutive', serif; font-size: 26px; line-height: 29px; font-weight: 400; position: absolute; left: 13px; top: 27px; }
  .category-label {
    position: absolute; left: 0; background: var(--forest-green);
    font-family: 'Cutive', serif; font-size: 28px; color: var(--ink);
    padding-left: 10px; display: flex; align-items: center;
  }
  .label-life { top: 136px; width: 268px; height: 57px; }
  .label-health { top: 483px; width: 339px; height: 56px; }
  .coaching-list { position: absolute; left: 42px; list-style: none; }
  .coaching-list li { font-size: 28px; height: 47.5px; display: flex; align-items: center; }
  .coaching-list li::before {
    content: ""; width: 17px; height: 17px; border-radius: 50%; background: var(--bullet);
    margin-right: 16px; flex: none;
  }
  .list-life { top: 222px; }
  .list-health { top: 570px; }
  .coaching-note {
    position: absolute; left: 0; bottom: 0; width: 371px; height: 124px;
    background: var(--deep-navy); color: var(--navy-note-text);
    font-size: 27px; line-height: 29px; text-align: justify; text-align-last: left;
    padding: 12px 14px 0 14px;
  }

  /* Right: weight loss */
  .panel-weight { left: 813px; width: 372px; background: var(--panel-bg); }
  .weight-title { position: absolute; left: 19px; top: 26px; font-family: 'Cutive', serif; font-size: 33px; line-height: 36px; font-weight: 400; }
  .weight-copy { position: absolute; left: 19px; width: 338px; font-weight: 300; font-size: 20px; line-height: 24px; color: var(--ink-soft); letter-spacing: -0.2px; }
  .copy-stats { top: 136px; }
  .copy-approach { top: 327px; }
  .copy-personal { top: 450px; }
  .copy-support { top: 679px; }
  .copy-ready { top: 739px; }
  .weight-question {
    position: absolute; left: 57px; top: 592px; width: 303px; height: 60px;
    background: var(--forest-green); font-size: 21px; color: var(--ink);
    display: flex; align-items: center; padding-left: 17px;
  }
</style>
</head>
<body>
  <section class="panel panel-areas">
    <div class="forest-backdrop" role="img" aria-label="Sunlit forest path among tall evergreen trees"></div>
    <div class="forest-veil"></div>
    <div class="areas-content">
      <h2 class="areas-title">Some of the<br>Coaching Areas<br>we focus on are:</h2>
      <ul class="areas-list">
        <li>Weight Loss</li>
        <li>Overwhelm/Time<br>Management</li>
        <li>Increased Energy</li>
        <li>Leadership</li>
        <li>Improved Relationships</li>
        <li>Finding Your Life Purpose<br>&amp; Passion</li>
        <li>Self Esteem &amp; Confidence</li>
      </ul>
    </div>
  </section>

  <section class="panel panel-coaching">
    <h2 class="coaching-title">We provide a full line<br>of Coaching Services</h2>
    <div class="category-label label-life">Life Coaching</div>
    <ul class="coaching-list list-life">
      <li>Relationships</li>
      <li>Life Purpose</li>
      <li>Confidence</li>
      <li>Overwhelm</li>
    </ul>
    <div class="category-label label-health">Health &amp; Wellness</div>
    <ul class="coaching-list list-health">
      <li>Weight Loss</li>
      <li>Energy</li>
      <li>Fitness</li>
    </ul>
    <p class="coaching-note">Coaching is customized and unique for your individual situation and circumstances.</p>
  </section>

  <section class="panel panel-weight">
    <h2 class="weight-title">Our Weight Loss<br>Program Works!</h2>
    <p class="weight-copy copy-stats">Over two thirds of American adults are overweight or obese. The average annual cost to the obese (BMI&gt;30) individual is approximately $4500. Over a lifetime obese people will die prematurely and pay approximately $100,000 more in medical expenses.</p>
    <p class="weight-copy copy-approach">The combination of a board certified Internal Medicine physician and a professional coach is a powerful and unique approach to help you achieve better health and well being.</p>
    <p class="weight-copy copy-personal">Each individual's path to wellness is unique. We offer a personalized approach to weight loss which helps you master eating, relapse and connecting your personal values to your lifestyle.</p>
    <div class="weight-question">Why do you want to lose weight?</div>
    <p class="weight-copy copy-support">We support you every step of the way. In the first month we will meet weekly one on one.</p>
    <p class="weight-copy copy-ready">We make sure you actually ready to make a change. We don't start unless you are sure the motivation to begin is coming from you and not something or someone else.</p>
  </section>
</body>
</html>
```